Self-Tanner Logo, Brand Concept and Bottle Label

We are developing a new Self-Tanner brand and are looking for a creative brand platform that will then be executed on a bottle - we are attaching the exact shape of the bottle from a brand called TovelBrisk. The platform we need will have three elements:

1. Logo
2. Color palette and design concept
3. The above applied to a bottle in either a label or a wrap

Please start with the logo and once we get that the rest can follow pretty directly. So we need a logo and to see how it would then be incorporated in a total package look on a bottle. So the wining design will be a total bottle look including a logo.

The three possible brands names are - at this point what we realy need is more submissions under the Lena Brokk name:

HoneyGlints
Amber Shore
Lena Brokk (this is the name of a Swedish blogger)

There are three names that we are considering so whichever combination of name and design is best will win. Please pick whichever name you think is most interesting see what kind of design it inspires.

Our primary target demographic is women aged 18-29. The next two targets are men 18-29 and women 29-44. So, its mostly women and mostly younger but we want to appeal to men and older consumers up to 44 years old. So the design can't be so totally female or young that we lose some people.

Many self-tanner brands use the colors yellow and brown in their executions. We are open to that but we are also open to other color patterns as well. I am attaching a mod page (Creative Concepts) that shows sun rays in case anybody finds that inspirational. If doing the Lena Brokk brand, please use a white background with neon pink letters and lime green accents.

Mostly what we need is a concept and package look that attracts attention when placed on shelf next to competitive pacakging. I am attaching pictures of 5 competitive brands (Competitive Pictures) - Bel Marno, Toffee Dune, Vessane, Nura Solanti and Outback Glow which is a bit more fun with the koala bear.
Updates

I have some really nice designs but I need a couple more under the Lena Brokk brand name and brand colors. I have very few of those and I want to make sure I have the best as that is one of our preferred directions.

Target Market(s)

Primary: Women 18-29
Secondary: Men 18-29

Logo Text

It should say either: HoneyGlints or Amber Shore (but not both). Or Lena Brokk.

Font styles to use
Sans Serif

Colors

Designer to choose colors to be used in the design.

Requirements
Must have
• One of the three brand names. Preferably Lena Brokk.
• She wants her main color to be a pink with an accent of a light green. As Lena is Swedish, the look of the bottle design and logo should be clean.
Nice to have
• The color palettes suggested in the brief

```html
<!DOCTYPE html>
<html lang="en">
<head>
<meta charset="utf-8">
<title>Amber Shore – Self Tanning Spray</title>
<link rel="stylesheet" href="https://fonts.googleapis.com/css2?family=Marcellus&family=Tenor+Sans&display=swap">
<style>
  :root {
    --paper: #ffffff;
    --ink: #353535;
    --tan: #d4ad6d;
    --lime: #dde04c;
  }
  html, body {
    margin: 0;
    padding: 0;
    overflow: hidden;
    background: var(--paper);
  }
  .label {
    position: relative;
    width: 1200px;
    height: 1001px;
    background: var(--paper);
    overflow: hidden;
  }
  .speckle-field {
    position: absolute;
    left: 0;
    bottom: 0;
    width: 1200px;
    height: 560px;
    background: radial-gradient(ellipse 900px 520px at 0% 100%,
      rgba(212, 173, 109, 0.55) 0%,
      rgba(212, 173, 109, 0.28) 45%,
      rgba(212, 173, 109, 0) 100%);
  }
  .brand-name {
    position: absolute;
    top: 260px;
    left: 0;
    width: 1200px;
    margin: 0;
    padding-left: 10px;
    box-sizing: border-box;
    text-align: center;
    font-family: "Marcellus", serif;
    font-weight: 400;
    font-size: 118px;
    line-height: 1;
    letter-spacing: 10px;
    color: var(--ink);
    white-space: nowrap;
  }
  .product-type {
    position: absolute;
    top: 415px;
    left: 0;
    width: 1200px;
    margin: 0;
    text-align: center;
    font-family: "Marcellus", serif;
    font-weight: 400;
    font-size: 100px;
    line-height: 1;
    letter-spacing: 7px;
    color: var(--tan);
    white-space: nowrap;
  }
  .product-format {
    position: absolute;
    top: 534px;
    left: 0;
    width: 1200px;
    margin: 0;
    padding-left: 4px;
    box-sizing: border-box;
    text-align: center;
    font-family: "Tenor Sans", sans-serif;
    font-size: 92px;
    line-height: 1;
    letter-spacing: 4px;
    color: var(--lime);
    white-space: nowrap;
  }
</style>
</head>
<body>
  <main class="label">
    <div class="speckle-field" role="img" aria-label="Scattered golden speckles drifting up from the lower left corner"></div>

    <p class="brand-name">AMBER SHORE</p>
    <h1 class="product-type">SELF TANNING</h1>
    <p class="product-format">SPRAY</p>
  </main>
</body>
</html>
```